Brass Kettle Business Card

I needed some business cards done for my band. We are a 9 piece funk/horn band that plays a lot of private parties, wedding receptions and music festivals. We'd like a design with vivid colors that incorporates our logo. You can check out our website at www.brasskettleband.com to see what type of vibe we are going for.

```html
<!DOCTYPE html>
<html lang="en">
<head>
<meta charset="utf-8">
<title>Brass Kettle Business Card</title>
<link href="https://fonts.googleapis.com/css2?family=Archivo:wght@400;700;800&display=swap" rel="stylesheet">
<style>
  :root {
    --page-bg: #2a2a2a;
    --ink: #0a0a0a;
    --lime: #c5d62e;
    --card-w: 540px;
    --card-h: 309px;
  }
  * { box-sizing: border-box; margin: 0; padding: 0; }
  html, body { width: 1200px; height: 750px; overflow: hidden; }
  body {
    background: var(--page-bg);
    font-family: "Archivo", Arial, sans-serif;
    display: flex;
    align-items: center;
    justify-content: center;
    gap: 40px;
  }
  .card {
    width: var(--card-w);
    height: var(--card-h);
    border-radius: 18px;
    position: relative;
    overflow: hidden;
  }
  .card-front {
    background: var(--ink);
    display: flex;
    align-items: center;
    justify-content: center;
  }
  .front-wordmark {
    color: var(--lime);
    font-weight: 800;
    font-size: 56px;
    letter-spacing: -0.5px;
  }
  .card-back { background: var(--lime); color: var(--ink); }
  .back-wordmark {
    position: absolute;
    top: 50px;
    right: 38px;
    font-weight: 800;
    font-size: 32px;
    letter-spacing: -0.3px;
  }
  .social-row {
    position: absolute;
    top: 108px;
    left: 36px;
    display: flex;
    gap: 4px;
  }
  .social-dot {
    width: 15px; height: 15px;
    border-radius: 50%;
    background: var(--ink);
  }
  .divider {
    position: absolute;
    left: 36px;
    right: 38px;
    top: 200px;
    height: 1px;
    background: var(--ink);
  }
  .person {
    position: absolute;
    left: 36px;
    bottom: 112px;
  }
  .person-name { font-weight: 700; font-size: 21px; line-height: 1.1; }
  .person-role { font-size: 13px; line-height: 1.3; }
  .contact-list {
    position: absolute;
    left: 36px;
    top: 212px;
    list-style: none;
    font-size: 13px;
    line-height: 1.55;
  }
  .contact-list li { display: flex; align-items: center; gap: 8px; }
  .contact-icon { width: 11px; height: 11px; flex: none; }
</style>
</head>
<body>
  <section class="card card-front">
    <div class="front-wordmark">Brass Kettle</div>
  </section>

  <section class="card card-back">
    <div class="back-wordmark">Brass Kettle</div>

    <div class="social-row" aria-label="Social media">
      <span class="social-dot"></span>
      <span class="social-dot"></span>
      <span class="social-dot"></span>
    </div>

    <div class="person">
      <div class="person-name">Marcus Reyes</div>
      <div class="person-role">President</div>
    </div>

    <div class="divider"></div>

    <ul class="contact-list">
      <li>
        <svg class="contact-icon" viewBox="0 0 12 12" aria-hidden="true">
          <path d="M2.5 0.8 L4.4 3.2 L3.4 4.4 Q4.6 6.9 7.6 8.6 L8.8 7.6 L11.2 9.5 L10 11.2 Q5.5 11.3 2.2 7.6 Q0.4 5 0.8 2 Z" fill="#0a0a0a"/>
        </svg>
        225.555.0182
      </li>
      <li>
        <svg class="contact-icon" viewBox="0 0 12 12" aria-hidden="true">
          <rect x="0.5" y="2" width="11" height="8" fill="#0a0a0a"/>
          <path d="M1 2.6 L6 6.6 L11 2.6" fill="none" stroke="#c5d62e" stroke-width="1.1"/>
        </svg>
        info@brasskettleband.com
      </li>
      <li>
        <svg class="contact-icon" viewBox="0 0 12 12" aria-hidden="true">
          <circle cx="6" cy="6" r="5.5" fill="#0a0a0a"/>
          <ellipse cx="6" cy="6" rx="2.2" ry="5.2" fill="none" stroke="#c5d62e" stroke-width="0.8"/>
          <line x1="0.8" y1="6" x2="11.2" y2="6" stroke="#c5d62e" stroke-width="0.8"/>
        </svg>
        www.brasskettleband.com
      </li>
    </ul>
  </section>
</body>
</html>
```